Seven Slides with Charts for Sales Presentation

We have the basic concept for seven important slides we need, but want to have them graphically pleasing beyond what we could do with standard charts and powerpoint. We are a software company. Attaching whiteboard versions of the slides and one graphic (slide 7). The graphics can be combined into animated slides, I will be happy to explain.

Target Market(s)

Decision Makers / Board Members for Professional Associations. For example, we are presenting to a State Association of Pharmacists next week.

Industry/Entity Type

Sales

Font styles to use
Sans Serif

Colors
33a6d7
00a990

Requirements
Must have
• Quality Graphics. I have more detail for the first slide too. You can look at http://dev.plumvessel.example for a sneak peek.
Nice to have
• Web "3.0" look and feel. Tablet / mobile friendly look.
Should not have
• Clip art or anything unprofessional.

```html
<!DOCTYPE html>
<html lang="en">
<head>
<meta charset="utf-8">
<title>Sales Presentation Slides</title>
<link href="https://fonts.googleapis.com/css2?family=Open+Sans:wght@300;400;600;700&display=swap" rel="stylesheet">
<style>
  :root {
    --page: #ffffff;
    --ink-light: #ffffff;
    --ink-dark: #14365a;
    --teal: #00a990;
    --teal-deep: #0b6d60;
    --sky: #33a6d7;
    --panel-line: #1c7e70;
    --body-grey: #555e66;
  }
  html, body {
    margin: 0;
    padding: 0;
    width: 1200px;
    height: 454px;
    overflow: hidden;
    background: var(--page);
    font-family: "Open Sans", Arial, sans-serif;
  }
  .deck { position: relative; width: 1200px; height: 454px; }
  .slide { position: absolute; width: 292px; height: 218px; display: block; }
  .slide-intro   { left: 5px;   top: 4px; }
  .slide-revenue { left: 305px; top: 4px; }
  .slide-proceeds{ left: 605px; top: 4px; }
  .slide-payout  { left: 905px; top: 4px; }
  .slide-ratings { left: 157px; top: 233px; }
  .slide-growth  { left: 458px; top: 233px; }
  .slide-quality { left: 758px; top: 233px; }
  .defs-holder { position: absolute; width: 0; height: 0; }

  text { font-family: "Open Sans", Arial, sans-serif; }
  .slide-title { fill: var(--ink-light); font-size: 14px; font-weight: 300; }
  .label-white { fill: var(--ink-light); }
  .pct { fill: var(--ink-light); font-size: 8px; font-weight: 300; }
  .brand-name { fill: var(--ink-dark); font-size: 8px; font-weight: 700; letter-spacing: 0.3px; }
  .brand-dot { fill: var(--ink-dark); }
  .panel-head { fill: var(--panel-line); font-size: 7px; font-weight: 400; }
  .col-head { fill: var(--panel-line); font-size: 5.5px; font-weight: 400; }
  .body-copy { fill: var(--body-grey); font-size: 3.2px; }
  .tiny { fill: var(--ink-light); font-size: 3.6px; }
  .cyl-text { fill: var(--ink-light); text-anchor: middle; font-weight: 300; }
  .divider { stroke: var(--ink-light); stroke-width: 0.8; fill: none; }
  .axis { stroke: var(--ink-light); stroke-width: 1.2; fill: none; }
  .grid { stroke: var(--ink-dark); stroke-width: 0.5; fill: none; }
  .matrix-head { fill: var(--ink-dark); font-size: 3.8px; text-anchor: middle; }
  .matrix-row { fill: var(--ink-light); font-size: 3.8px; }
  .legend-name { fill: var(--ink-light); font-size: 13px; font-weight: 300; }
  .legend-note { fill: var(--ink-light); font-size: 4.2px; }
  .stars { fill: var(--ink-light); font-size: 6px; letter-spacing: 0.6px; }
</style>
</head>
<body>
<main class="deck">

  <svg class="defs-holder" aria-hidden="true">
    <defs>
      <linearGradient id="slide-bg" x1="0" y1="0" x2="0" y2="1">
        <stop offset="0" stop-color="#1b2262"/>
        <stop offset="0.45" stop-color="#3668b0"/>
        <stop offset="1" stop-color="#6fc4ee"/>
      </linearGradient>
      <linearGradient id="cyl-body" x1="0" y1="0" x2="1" y2="0">
        <stop offset="0" stop-color="#0b6d60"/>
        <stop offset="0.45" stop-color="#8fe6d0"/>
        <stop offset="1" stop-color="#0a6a5c"/>
      </linearGradient>
      <linearGradient id="cyl-top" x1="0" y1="0" x2="0" y2="1">
        <stop offset="0" stop-color="#c6f5e8"/>
        <stop offset="1" stop-color="#3fb89e"/>
      </linearGradient>
      <radialGradient id="pie-fill" cx="0.5" cy="0.6" r="0.6">
        <stop offset="0" stop-color="#2bbf9d"/>
        <stop offset="0.7" stop-color="#7fdcc6"/>
        <stop offset="1" stop-color="#e8faf5"/>
      </radialGradient>
      <linearGradient id="wedge-fill" x1="0" y1="1" x2="1" y2="0">
        <stop offset="0" stop-color="#e3f8f2"/>
        <stop offset="0.5" stop-color="#5fcfb4"/>
        <stop offset="1" stop-color="#0f7d6c"/>
      </linearGradient>
      <radialGradient id="dot-fill">
        <stop offset="0" stop-color="#ffffff"/>
        <stop offset="0.45" stop-color="#1fb396"/>
        <stop offset="1" stop-color="#0b6d60"/>
      </radialGradient>
    </defs>
  </svg>

  <!-- Slide 1: introduction -->
  <svg class="slide slide-intro" viewBox="0 0 292 218">
    <rect width="292" height="218" fill="url(#slide-bg)"/>
    <rect x="122" y="10" width="40" height="40" rx="20" fill="#dfe6f2" opacity="0.35" role="img" aria-label="Rocket illustration"/>
    <text class="label-white" x="146" y="66" text-anchor="middle" font-size="11.5" font-weight="300">KR Association of Rocket Scientists</text>
    <text class="label-white" x="146" y="76" text-anchor="middle" font-size="5.5" font-weight="300">Finding the best instruction for you.</text>
    <rect x="16" y="85" width="260" height="94" fill="#ffffff" stroke="var(--panel-line)" stroke-width="1.5"/>
    <text class="panel-head" x="146" y="96" text-anchor="middle">HOW DOES IT WORK?</text>
    <line x1="20" y1="99" x2="272" y2="99" stroke="var(--panel-line)" stroke-width="0.5"/>
    <line x1="146" y1="102" x2="146" y2="175" stroke="var(--panel-line)" stroke-width="0.5"/>
    <text class="col-head" x="20" y="108">Instructors Compete, You Win</text>
    <text class="col-head" x="150" y="108">Your Learning Style</text>
    <g class="body-copy">
      <text x="20" y="115">Anyone who makes great lessons can post them</text>
      <text x="20" y="119.5">on our site. Unlike the classroom, instructors</text>
      <text x="20" y="124">here compete with each other for your ratings,</text>
      <text x="20" y="128.5">reviews and views, driving up quality and</text>
      <text x="20" y="133">teaching engagement. The results put the best</text>
      <text x="20" y="137.5">instructors first, so you only find them all here.</text>
      <text x="20" y="142">They have already made thousands of lessons</text>
      <text x="20" y="146.5">and courses on every topic, with more coming</text>
      <text x="20" y="151">out every day.</text>
      <text x="150" y="115">Some like step-by-step courses, where each lesson</text>
      <text x="150" y="119.5">builds on the last. Others prefer to browse, where</text>
      <text x="150" y="124">the student chooses what to learn and when. Some</text>
      <text x="150" y="128.5">just want to learn one skill at their own level.</text>
      <text x="150" y="133">Some like learning to read notes from textbooks.</text>
      <text x="150" y="137.5">Others are interested in a particular genre or style.</text>
      <text x="150" y="142">Some get to the point quickly, others prefer to</text>
      <text x="150" y="146.5">have things explained thoroughly. No matter your</text>
      <text x="150" y="151">style, our reviews help you find what is best for you.</text>
    </g>
    <circle class="brand-dot" cx="12" cy="200" r="2.6"/>
    <text class="brand-name" x="18" y="203">VELQUARA</text>
  </svg>

  <!-- Slide 2: revenue allocation -->
  <svg class="slide slide-revenue" viewBox="0 0 292 218">
    <rect width="292" height="218" fill="url(#slide-bg)"/>
    <text class="slide-title" x="18" y="24">Revenue Allocation</text>
    <path d="M76 42 V185 A71 10 0 0 0 218 185 V42 Z" fill="url(#cyl-body)"/>
    <ellipse cx="147" cy="42" rx="71" ry="10" fill="url(#cyl-top)"/>
    <path class="divider" d="M76 72 A71 10 0 0 0 218 72"/>
    <path class="divider" d="M76 83 A71 10 0 0 0 218 83"/>
    <path class="divider" d="M76 88 A71 10 0 0 0 218 88"/>
    <text class="cyl-text" x="147" y="52" font-size="7">Software License</text>
    <text class="cyl-text" x="147" y="61" font-size="7">Accounting</text>
    <text class="cyl-text" x="147" y="70" font-size="7">Administration</text>
    <text class="cyl-text" x="147" y="87" font-size="7">Advertising</text>
    <text class="cyl-text" x="147" y="136" font-size="14">PROCEEDS</text>
    <text class="pct" x="48" y="72">25%</text>
    <text class="pct" x="52" y="93">10%</text>
    <text class="pct" x="50" y="102">3-5%</text>
    <line x1="222" y1="96" x2="232" y2="96" stroke="var(--ink-dark)" stroke-width="0.6"/>
    <path d="M216 96 L222 93.5 L222 98.5 Z" fill="var(--ink-dark)"/>
    <text class="tiny" x="234" y="94">Credit Card Transaction Fees</text>
    <text class="tiny" x="234" y="99">Association Specific Expenses</text>
    <circle class="brand-dot" cx="216" cy="203" r="2.6"/>
    <text class="brand-name" x="222" y="206">VELQUARA</text>
  </svg>

  <!-- Slide 3: proceeds -->
  <svg class="slide slide-proceeds" viewBox="0 0 292 218">
    <rect width="292" height="218" fill="url(#slide-bg)"/>
    <text class="slide-title" x="270" y="24" text-anchor="end">Proceeds</text>
    <path d="M76 56 V184 A70 10 0 0 0 216 184 V56 Z" fill="url(#cyl-body)"/>
    <ellipse cx="146" cy="56" rx="70" ry="10" fill="url(#cyl-top)"/>
    <path class="divider" d="M76 76 A70 10 0 0 0 216 76"/>
    <text class="cyl-text" x="146" y="60" font-size="8.5">Paid to Association</text>
    <text class="cyl-text" x="146" y="118" font-size="11">KR Contribution</text>
    <text class="cyl-text" x="146" y="130" font-size="11">to</text>
    <text class="cyl-text" x="146" y="142" font-size="11">Instructor Payout</text>
    <text class="cyl-text" x="146" y="154" font-size="11">Pool</text>
    <text class="pct" x="50" y="72">25%</text>
    <text class="pct" x="50" y="125">75%</text>
    <circle class="brand-dot" cx="10" cy="203" r="2.6"/>
    <text class="brand-name" x="16" y="206">VELQUARA</text>
  </svg>

  <!-- Slide 4: instructor payout pool -->
  <svg class="slide slide-payout" viewBox="0 0 292 218">
    <rect width="292" height="218" fill="url(#slide-bg)"/>
    <text class="slide-title" x="18" y="24">Instructor Payout</text>
    <text class="slide-title" x="18" y="40">Pool</text>
    <circle cx="146" cy="118" r="72" fill="url(#pie-fill)"/>
    <line x1="146" y1="118" x2="146" y2="46" stroke="#ffffff" stroke-width="1.2"/>
    <line x1="146" y1="118" x2="83.6" y2="154" stroke="#ffffff" stroke-width="1.2"/>
    <line x1="146" y1="118" x2="208.4" y2="154" stroke="#ffffff" stroke-width="1.2"/>
    <text class="label-white" x="112" y="86" text-anchor="middle" font-size="11">Sally</text>
    <text class="label-white" x="112" y="98" text-anchor="middle" font-size="7">33%</text>
    <text class="label-white" x="174" y="86" text-anchor="middle" font-size="11">Johnny</text>
    <text class="label-white" x="174" y="98" text-anchor="middle" font-size="7">33%</text>
    <text class="label-white" x="146" y="146" text-anchor="middle" font-size="11">George</text>
    <text class="label-white" x="146" y="158" text-anchor="middle" font-size="7">33%</text>
    <circle class="brand-dot" cx="216" cy="203" r="2.6"/>
    <text class="brand-name" x="222" y="206">VELQUARA</text>
  </svg>

  <!-- Slide 5: ratings-based split -->
  <svg class="slide slide-ratings" viewBox="0 0 292 218">
    <rect width="292" height="218" fill="url(#slide-bg)"/>
    <circle cx="93" cy="110" r="76" fill="url(#pie-fill)"/>
    <line x1="93" y1="110" x2="93" y2="34" stroke="#ffffff" stroke-width="1.2"/>
    <line x1="93" y1="110" x2="165.3" y2="133.5" stroke="#ffffff" stroke-width="1.2"/>
    <line x1="93" y1="110" x2="167.9" y2="123" stroke="#ffffff" stroke-width="1.2"/>
    <text class="label-white" x="122" y="78" text-anchor="middle" font-size="11">George</text>
    <text class="label-white" x="122" y="90" text-anchor="middle" font-size="7">25%</text>
    <text class="label-white" x="70" y="110" text-anchor="middle" font-size="13">Sally</text>
    <text class="label-white" x="70" y="123" text-anchor="middle" font-size="7">70%</text>
    <text class="label-white" x="178" y="153" text-anchor="middle" font-size="10">Johnny</text>
    <text class="label-white" x="178" y="166" text-anchor="middle" font-size="7">5%</text>
    <line x1="176" y1="138" x2="168" y2="128" stroke="var(--ink-dark)" stroke-width="0.7"/>
    <path d="M166 125 L171 128 L167.5 131 Z" fill="var(--ink-dark)"/>
    <text class="legend-name" x="214" y="52">Sally</text>
    <text class="stars" x="214" y="62">★★★★★</text>
    <text class="legend-note" x="214" y="70">"Engaging"</text>
    <text class="legend-note" x="214" y="77">"Timely"</text>
    <text class="legend-note" x="214" y="84">"Highly relevant"</text>
    <text class="legend-name" x="214" y="109">George</text>
    <text class="stars" x="214" y="118">★★★</text>
    <text class="legend-note" x="214" y="126">"Entertaining"</text>
    <text class="legend-note" x="214" y="133">"Dated"</text>
    <text class="legend-name" x="214" y="152">Johnny</text>
    <text class="stars" x="214" y="162">★★</text>
    <circle class="brand-dot" cx="12" cy="203" r="2.6"/>
    <text class="brand-name" x="18" y="206">VELQUARA</text>
  </svg>

  <!-- Slide 6: growth phases -->
  <svg class="slide slide-growth" viewBox="0 0 292 218">
    <rect width="292" height="218" fill="url(#slide-bg)"/>
    <text class="label-white" x="34" y="42" text-anchor="middle" font-size="12" font-weight="300">Quantity</text>
    <text class="label-white" x="34" y="55" text-anchor="middle" font-size="12" font-weight="300">of</text>
    <text class="label-white" x="34" y="68" text-anchor="middle" font-size="12" font-weight="300">Lessons</text>
    <path class="axis" d="M34 78 V182 H200"/>
    <path d="M30 84 L34 76 L38 84" class="axis"/>
    <path d="M194 178 L202 182 L194 186" class="axis"/>
    <path d="M52 162 L256 26 V162 Z" fill="url(#wedge-fill)"/>
    <line x1="114" y1="121" x2="114" y2="162" stroke="var(--teal-deep)" stroke-width="0.8"/>
    <line x1="183" y1="75" x2="183" y2="162" stroke="var(--teal-deep)" stroke-width="0.8"/>
    <line x1="114" y1="96" x2="114" y2="119" stroke="var(--ink-dark)" stroke-width="0.4" stroke-dasharray="1 1"/>
    <line x1="183" y1="44" x2="183" y2="73" stroke="var(--ink-dark)" stroke-width="0.4" stroke-dasharray="1 1"/>
    <text class="tiny" x="114" y="87" text-anchor="middle">Competition</text>
    <text class="tiny" x="114" y="92" text-anchor="middle">Ensues</text>
    <text class="tiny" x="183" y="35" text-anchor="middle">Quality</text>
    <text class="tiny" x="183" y="40" text-anchor="middle">Saturation</text>
    <text class="label-white" x="96" y="156" text-anchor="middle" font-size="10" font-weight="300">Phase I</text>
    <text class="label-white" x="150" y="134" text-anchor="middle" font-size="10" font-weight="300">Phase II</text>
    <text class="label-white" x="218" y="108" text-anchor="middle" font-size="10" font-weight="300">Phase III</text>
    <text class="tiny" x="84" y="170" text-anchor="middle">Higher Convenience</text>
    <text class="tiny" x="84" y="175" text-anchor="middle">Current Standards</text>
    <text class="tiny" x="148" y="170" text-anchor="middle">Competition Drives</text>
    <text class="tiny" x="148" y="175" text-anchor="middle">Quality Improvement</text>
    <text class="tiny" x="220" y="170" text-anchor="middle">Diversification &amp;</text>
    <text class="tiny" x="220" y="175" text-anchor="middle">Specialization</text>
    <text class="label-white" x="62" y="204" font-size="12" font-weight="300">Time</text>
    <circle class="brand-dot" cx="216" cy="203" r="2.6"/>
    <text class="brand-name" x="222" y="206">VELQUARA</text>
  </svg>

  <!-- Slide 7: quality control matrix -->
  <svg class="slide slide-quality" viewBox="0 0 292 218">
    <rect width="292" height="218" fill="url(#slide-bg)"/>
    <text class="slide-title" x="274" y="24" text-anchor="end">Quality Control Matrix</text>
    <g class="matrix-head">
      <text x="82" y="64">APPROVE</text>
      <text x="82" y="69">EVERYTHING</text>
      <text x="131" y="64">AUTO-APPROVE</text>
      <text x="131" y="69">BY REQUIREMENTS</text>
      <text x="180" y="64">SUGGEST APPROVAL</text>
      <text x="180" y="69">BY REQUIREMENTS</text>
      <text x="229" y="64">APPROVE</text>
      <text x="229" y="69">MANUALLY</text>
    </g>
    <rect x="58" y="76" width="196" height="92" fill="#ffffff"/>
    <path class="grid" d="M58 76 H254 V168 H58 Z M107 76 V168 M156 76 V168 M205 76 V168 M58 106.7 H254 M58 137.3 H254"/>
    <text class="matrix-row" x="20" y="93">PUBLISHER</text>
    <text class="matrix-row" x="20" y="124">INSTRUCTOR</text>
    <text class="matrix-row" x="20" y="155">LESSON</text>
    <circle cx="81" cy="91" r="7" fill="url(#dot-fill)"/>
    <circle cx="130" cy="122" r="7" fill="url(#dot-fill)"/>
    <circle cx="179" cy="152" r="7" fill="url(#dot-fill)"/>
    <circle class="brand-dot" cx="12" cy="203" r="2.6"/>
    <text class="brand-name" x="18" y="206">VELQUARA</text>
  </svg>

</main>
</body>
</html>
```